Business Cards

I am a landscape designer and I am hired to do over the top landscapes!
I pay attention to detail and do everything from growing my own orchids and Fruits and Vegetables.
I build ponds water features. I do Landscape Lighting and Specialize in Drip Irrigation for New Landscapes.
I am looking for something with a picture of one of my landscapes and pictures of Orchids on the back so I can work on growing my Orchid business.
I like the plastic cards.
I like Saturation
I like color and I want something that really sticks out!
I will attach a few pics!
Thanks
Corey
A Bright Terrace LLC
Corey Valdrup
Orchids & Organic Farming
Landscaping Made Simple
555-204-7193
Abrightterrace@mailnest.example
Coral Vista FL

Target Market(s)

I work for Wealthy Clients who want unique designs and enjoy rare plants.
I am the goto guy for tropical and rare plants
Cool Designs
Orchids
Interior Decorating
Exterior Lighting
Organic Farming
People who appreciate plants

Industry/Entity Type

Landscape

Font styles to use
Decorative

Requirements
Must have
• COLOR COLOR COLOR
Saturation
Sleek and Clean
Should not have
• tacky

```html
<!DOCTYPE html>
<html lang="en">
<head>
<meta charset="utf-8">
<title>A Bright Terrace LLC – Business Cards</title>
<link rel="stylesheet" href="https://fonts.googleapis.com/css2?family=Bebas+Neue&family=Oswald:wght@500&display=swap">
<style>
  :root {
    --page-bg: #e9e4dc;
    --card-white: #ffffff;
    --band-black: #0d0a0a;
    --leaf-dark: #1f5a12;
    --leaf-mid: #3f9a1e;
    --leaf-light: #8fd23a;
    --bloom-red: #d8342a;
    --accent-orange: #f26a10;
    --accent-green: #22a019;
    --contact-green: #6ee01a;
    --text-white: #ffffff;
    --orchid-magenta: #c2187a;
    --orchid-yellow: #f3c316;
    --orchid-violet: #5a2bd6;
    --orchid-coral: #f2602a;
  }
  * { margin: 0; padding: 0; box-sizing: border-box; }
  html, body { width: 1200px; height: 900px; overflow: hidden; }
  body { background: var(--page-bg); position: relative; font-family: "Bebas Neue", "Oswald", sans-serif; }

  .card {
    position: absolute; left: 276px; width: 646px; height: 367px;
    overflow: hidden; box-shadow: 0 3px 10px rgba(0,0,0,.25);
  }
  .card-front { top: 48px; background: var(--card-white); }
  .card-back { top: 481px; background: var(--band-black); }

  .company-name {
    position: absolute; left: 22px; top: 16px;
    font-size: 148px; line-height: 112px; letter-spacing: 2px;
    text-transform: uppercase; font-weight: 400;
    background: linear-gradient(135deg, var(--leaf-mid) 0%, var(--leaf-dark) 30%, var(--bloom-red) 45%, var(--leaf-light) 60%, var(--leaf-dark) 85%, var(--leaf-mid) 100%);
    -webkit-background-clip: text; background-clip: text;
    color: transparent; -webkit-text-fill-color: transparent;
  }
  .tagline {
    position: absolute; left: 184px; top: 242px;
    font-family: "Oswald", sans-serif; font-weight: 500;
    font-size: 27px; line-height: 31px; letter-spacing: 1px;
    color: var(--accent-orange); text-transform: uppercase;
  }
  .services {
    position: absolute; left: 184px; top: 326px;
    font-size: 22px; letter-spacing: 1.4px;
    color: var(--accent-green); text-transform: uppercase; white-space: nowrap;
  }

  .orchid-grid { position: absolute; inset: 0 0 121px 0; }
  .orchid-photo { position: absolute; }
  .orchid-magenta { left: 0; top: 0; width: 215px; height: 246px;
    background: radial-gradient(circle at 45% 45%, #e0309a, var(--orchid-magenta) 50%, #3d7a2a 100%); }
  .orchid-yellow { left: 215px; top: 0; width: 216px; height: 122px;
    background: radial-gradient(circle at 45% 50%, #ffe04a, var(--orchid-yellow) 55%, #e4621a 100%); }
  .orchid-violet { left: 215px; top: 122px; width: 216px; height: 124px;
    background: radial-gradient(circle at 40% 45%, #8250f0, var(--orchid-violet) 55%, #2a1a6a 100%); }
  .orchid-coral { left: 431px; top: 0; width: 215px; height: 246px;
    background: radial-gradient(circle at 50% 55%, #ff9a3a, var(--orchid-coral) 50%, #2e4a1a 100%); }

  .contact-band { position: absolute; left: 0; right: 0; bottom: 0; height: 121px; padding: 14px 0 0 20px; }
  .person-name { font-size: 58px; line-height: 60px; color: var(--text-white); letter-spacing: 1px; text-transform: uppercase; font-weight: 400; }
  .contact-line { margin-top: 8px; font-size: 21px; letter-spacing: .8px; text-transform: uppercase; white-space: nowrap; }
  .contact-line .city { color: var(--text-white); margin-right: 10px; }
  .contact-line .phone, .contact-line .email { color: var(--contact-green); }
  .contact-line .phone { margin-right: 14px; }
</style>
</head>
<body>
  <section class="card card-front">
    <h1 class="company-name">A Bright<br>Terrace<br>LLC</h1>
    <p class="tagline">We make gardens bold<br>and beautiful.</p>
    <p class="services">Landscape design &amp; build, lighting &amp; drip irrigation</p>
  </section>

  <section class="card card-back">
    <div class="orchid-grid">
      <div class="orchid-photo orchid-magenta" role="img" aria-label="Photo of magenta orchid sprays"></div>
      <div class="orchid-photo orchid-yellow" role="img" aria-label="Close-up photo of a yellow orchid bloom"></div>
      <div class="orchid-photo orchid-violet" role="img" aria-label="Photo of violet spotted orchids"></div>
      <div class="orchid-photo orchid-coral" role="img" aria-label="Photo of orange and pink orchid cluster"></div>
    </div>
    <div class="contact-band">
      <h2 class="person-name">Corey Valdrup</h2>
      <p class="contact-line">
        <span class="city">Coral Vista FL</span>
        <span class="phone">T. 555-204-7193</span>
        <span class="email">E. Abrightterrace@mailnest.example</span>
      </p>
    </div>
  </section>
</body>
</html>
```